Organic Soap Packaging

We need a package design for a new company called Fern Naturals. Our primary product is organic soap. Our business model is based on the social entrepreneurial concept of by one give one like Valo shoes. We are giving soap to help prevent the spread of disease; 1.4 million deaths a year can be prevented by hand washing.

The design is for a recycled cardboard box/package. We want to demonstrate the high end, luxury feel of the product with undertones of organic/earth friendly/social conscious.

The soap is small batch, spa like, essential oil scented all natural luxury.
Updates

I am very excited about this startup business and I believe we will have great success! I am passionate about organic personal care and helping others in need. If you share my passion, please bring your work to the table!

Target Market(s)

My target market is people who are educated through college. Health conscious, socially conscious, Generation X. Basically shoppers of Green Basket and Halvorsen.

Industry/Entity Type

Business

Requirements
Must have
• Suitable for Face, Hair, and Skin
Scented with Organic Essential Oils

```html
<!DOCTYPE html>
<html lang="en">
<head>
<meta charset="utf-8">
<title>Fern Naturals – Luxury Organic Soap Package Front</title>
<link rel="stylesheet" href="https://fonts.googleapis.com/css2?family=EB+Garamond:ital,wght@0,400;0,500;0,600;1,400;1,600&display=swap">
<style>
  :root {
    --page-bg: #ffffff;
    --kraft: #c4b5a2;
    --kraft-dark: #b5a590;
    --ink: #2f2c2a;
    --frame: #4a4744;
    --leaf: #6fa23a;
    --leaf-light: #a9d16a;
    --leaf-dark: #3f7a22;
  }
  * { box-sizing: border-box; margin: 0; padding: 0; }
  html, body {
    width: 1200px; height: 927px; overflow: hidden;
    background: var(--page-bg);
  }
  body { position: relative; font-family: "EB Garamond", Georgia, serif; color: var(--ink); }

  .package-front {
    position: absolute; left: 335px; top: 20px;
    width: 530px; height: 887px;
    background: radial-gradient(ellipse at 50% 40%, var(--kraft) 0%, var(--kraft-dark) 100%);
    box-shadow: 0 2px 6px rgba(0,0,0,.25);
  }
  .brand-mark {
    position: absolute; left: 18px; top: 42px;
    display: flex; align-items: center; gap: 8px;
    font-size: 32px; font-weight: 500; color: var(--leaf); line-height: 1;
  }
  .brand-mark .dot { width: 22px; height: 22px; background: var(--leaf-light); border-radius: 50%; }
  .frame {
    position: absolute; left: 20px; top: 96px; right: 20px; bottom: 18px;
    border: 2px solid var(--frame); border-radius: 14px;
  }
  .plant-illustration {
    position: absolute; left: 40px; top: 170px; width: 450px; height: 470px;
    border-radius: 40% 40% 20% 20%;
    background:
      radial-gradient(ellipse 55% 14% at 40% 92%, rgba(185,173,160,.9), transparent 70%),
      radial-gradient(ellipse 60% 60% at 50% 45%, rgba(111,162,58,.55), rgba(169,209,106,.25) 60%, transparent 80%);
  }
  .title {
    position: absolute; left: 0; right: 0; top: 112px; text-align: center;
    font-size: 29px; font-weight: 500; letter-spacing: 1.5px;
  }
  .subtitle {
    position: absolute; left: 0; right: 0; top: 152px; text-align: center; font-size: 20px;
  }
  .suitable-label {
    position: absolute; left: 0; right: 0; top: 262px; text-align: center;
    font-size: 23px; font-style: italic; font-weight: 600; color: var(--leaf-dark);
  }
  .uses {
    position: absolute; left: 0; right: 0; top: 288px; text-align: center;
    font-size: 33px; font-weight: 500; letter-spacing: 2px;
  }
  .weight {
    position: absolute; right: 40px; top: 348px; font-size: 19px; letter-spacing: .5px;
  }
  .brand-inline {
    position: absolute; right: 38px; top: 488px;
    display: flex; align-items: center; gap: 6px;
    font-size: 24px; font-weight: 500; color: var(--leaf); line-height: 1;
  }
  .brand-inline .dot { width: 14px; height: 14px; background: var(--leaf-light); border-radius: 50%; }
  .give-equation {
    position: absolute; left: 0; right: 0; top: 636px;
    text-align: center; font-size: 24px; line-height: 1;
  }
  .mission {
    position: absolute; left: 32px; right: 30px; top: 676px;
    font-size: 18.5px; line-height: 1.28;
  }
  .mission .brand-name { font-weight: 600; color: var(--leaf); }
  .mission em { font-style: italic; font-weight: 600; }
</style>
</head>
<body>
  <main class="package-front">
    <div class="brand-mark"><span class="dot"></span>Fern Naturals</div>
    <div class="frame"></div>
    <div class="plant-illustration" role="img" aria-label="Illustration of a green seedling with three dewy leaves rising from a water ripple"></div>

    <h1 class="title">LUXURY ORGANIC SOAP</h1>
    <p class="subtitle">Scented With Organic Essential Oils</p>
    <p class="suitable-label">Suitable For</p>
    <p class="uses">FACE • HAIR • SKIN</p>
    <p class="weight">120g | 4.25 oz</p>

    <div class="brand-inline"><span class="dot"></span>Fern Naturals</div>

    <p class="give-equation">one = one</p>

    <p class="mission">
      <span class="brand-name">Fern Naturals</span> is passionate about organic personal care and helping others in need. We are <em>giving</em> soap to help prevent the spread of disease; <em>1.4 million deaths a year can be prevented by hand washing.</em> When you <em>buy one</em> bar of Fern Naturals soap, we <em>give one</em> to those in need. Together we can make this world a cleaner, healthier and happier place to live.
    </p>
  </main>
</body>
</html>
```